Business Card Design Project

We are a distribution company providing goods to Latin America. We sell everything from Medical equipment, generic medicines, to carecliners. The logo that we use is attached. The logo can incorporate different colors other than black for versatility. The company name is Valdren Global Enterprises and/or VGE. The card will be printed using 1 or more of the following: Silk mounted and/or embossed. So if the design ideas could be made to incorporate that technique or any other unique techniques, it would be great. The target market is dialysis centers/doctors.

Basic Info for card:
Marna Dowell
Purchasing Manager
417-305-6184 direct
417-521-7790 fax
marna.dowell@valdrenvge.example
www.valdrenvge.example

Target Market(s)

Latin America

Industry/Entity Type

Business

Requirements
Nice to have
• The Front of the card should have the basic contact information with company name/logo. The back of the card could incorporate

```html
<!DOCTYPE html>
<html lang="en">
<head>
<meta charset="utf-8">
<title>Marna Dowell — Business Card</title>
<link rel="stylesheet" href="https://fonts.googleapis.com/css2?family=Cormorant+SC:wght@500;600&family=EB+Garamond:wght@400&display=swap">
<style>
  :root {
    --backdrop: #efefef;
    --card-plum: #3f1b3b;
    --card-plum-light: #4a2346;
    --card-plum-deep: #321530;
    --rule-dark: #2a1027;
    --rule-light: #5a3256;
    --mark-sage: #7f9993;
    --ink-white: #f4f1f4;
    --ink-soft: #d9d0d8;
  }
  * { margin: 0; padding: 0; box-sizing: border-box; }
  html, body {
    width: 1199px;
    height: 1200px;
    overflow: hidden;
    background: var(--backdrop);
  }
  .canvas {
    position: relative;
    width: 1199px;
    height: 1200px;
  }
  .card {
    position: absolute;
    left: 75px;
    top: 300px;
    width: 1050px;
    height: 600px;
    background: linear-gradient(160deg, var(--card-plum-light) 0%, var(--card-plum) 45%, var(--card-plum-deep) 100%);
    box-shadow: 0 12px 30px rgba(0,0,0,0.18);
    color: var(--ink-white);
  }
  .divider {
    position: absolute;
    left: 0;
    right: 0;
    top: 292px;
    height: 4px;
    border-top: 2px solid var(--rule-dark);
    border-bottom: 2px solid var(--rule-light);
  }
  .brand-mark {
    position: absolute;
    left: 70px;
    top: 70px;
    display: flex;
    align-items: center;
    gap: 18px;
    color: var(--mark-sage);
    font-family: "Cormorant SC", serif;
    font-weight: 600;
    font-size: 96px;
    letter-spacing: 6px;
    line-height: 1;
  }
  .brand-mark .dot {
    width: 40px;
    height: 40px;
    border-radius: 50%;
    background: var(--mark-sage);
  }
  .brand-name {
    position: absolute;
    left: 72px;
    top: 190px;
    color: var(--mark-sage);
    font-family: "Cormorant SC", serif;
    font-weight: 600;
    font-size: 26px;
    letter-spacing: 3px;
  }
  .identity {
    position: absolute;
    right: 70px;
    top: 170px;
    text-align: right;
    font-family: "Cormorant SC", serif;
    line-height: 1;
  }
  .identity .person {
    font-weight: 600;
    font-size: 60px;
    letter-spacing: 2px;
  }
  .identity .role {
    margin-top: 4px;
    font-weight: 500;
    font-size: 24px;
    letter-spacing: 1.5px;
    color: var(--ink-soft);
  }
  .address {
    position: absolute;
    left: 70px;
    right: 70px;
    top: 318px;
    font-family: "Cormorant SC", serif;
    font-weight: 600;
    font-size: 30px;
    letter-spacing: 9px;
    white-space: nowrap;
  }
  .online {
    position: absolute;
    right: 70px;
    top: 378px;
    text-align: right;
    font-family: "EB Garamond", serif;
    font-size: 28px;
    line-height: 1.3;
  }
  .direct {
    position: absolute;
    left: 70px;
    bottom: 52px;
    font-family: "EB Garamond", serif;
    font-size: 34px;
    line-height: 1.3;
  }
</style>
</head>
<body>
<main class="canvas">
  <section class="card" aria-label="Business card front">
    <div class="brand-mark"><span class="dot"></span><span>VGE</span></div>
    <div class="brand-name">Valdren Global Enterprises</div>

    <div class="identity">
      <div class="person">Marna Dowell</div>
      <div class="role">Purchasing Manager</div>
    </div>

    <div class="divider"></div>

    <p class="address">1870 Harbor Crest Lane Miami, FL 33190</p>

    <div class="online">
      <div class="email">marna.dowell@valdrenvge.example</div>
      <div class="web">www.valdrenvge.example</div>
    </div>

    <div class="direct">
      <div class="phone">Phone 417.305.6184</div>
      <div class="fax">Fax 417.521.7790</div>
    </div>
  </section>
</main>
</body>
</html>
```